Professional Home Buyer business card needed

I need a pretty straight forward business card designed. We help people that NEED to sell their homes solve problems. We perform all types of Real Estate transactions including flip, wholesale, investment, rental property and multi family. The card will mainly be used to give to prospective Sellers but will also be given to Real Estate Investors as well. It should professional and very easy to read, most clients are older people.

Target Market(s)

Distressed home sellers as well as Real Estate investors

Industry/Entity Type

Real Estate

Contact Information for Business Card

should be a professional layout

Colors
ec1f27
ffffff
000000

Requirements
Must have
• Large logo on back and smaller one on front. should utilize Red, white, and black.
• I am thinking of using a soft touch coating on the card so keep that in mind.
• Contact info should be very easy to read, think older clients.
Nice to have
• I would like to see a design with rounded corners on the card
Should not have
• pictures of homes or other home graphics.

```html
<!DOCTYPE html>
<html lang="en">
<head>
<meta charset="utf-8">
<title>Keystone Home Buyers – Business Card</title>
<link rel="stylesheet" href="https://fonts.googleapis.com/css2?family=Roboto:wght@400;500;700&family=Archivo+Black&display=swap">
<style>
  :root {
    --red: #ec1f27;
    --white: #ffffff;
    --black: #000000;
    --stage: #6d767b;
    --muted: #d9d9d9;
  }
  * { box-sizing: border-box; margin: 0; padding: 0; }
  html, body { width: 1200px; height: 900px; overflow: hidden; }
  body {
    background: var(--stage);
    font-family: "Roboto", Arial, sans-serif;
    display: flex;
    align-items: center;
    justify-content: center;
    gap: 50px;
  }
  .card {
    position: relative;
    width: 525px;
    height: 300px;
    border-radius: 14px;
    overflow: hidden;
    background: var(--black);
  }

  /* Back of card: large brand */
  .card-back {
    display: flex;
    flex-direction: column;
    align-items: center;
    justify-content: center;
    color: var(--white);
  }
  .brand-large {
    display: flex;
    align-items: center;
    gap: 14px;
    font-family: "Archivo Black", Arial, sans-serif;
    font-size: 44px;
    letter-spacing: 2px;
    color: var(--white);
    text-transform: uppercase;
  }
  .brand-large .brand-dot {
    width: 26px; height: 26px; border-radius: 50%;
    background: var(--red);
  }
  .brand-sub {
    font-family: "Archivo Black", Arial, sans-serif;
    font-size: 26px;
    letter-spacing: 8px;
    margin-top: 6px;
    text-transform: uppercase;
  }
  .back-web {
    margin-top: 26px;
    font-size: 15px;
    color: var(--muted);
  }

  /* Front of card */
  .card-front { background: var(--black); }
  .front-shape { position: absolute; inset: 0; }
  .brand-small {
    position: absolute;
    left: 30px; top: 26px;
    display: flex; align-items: center; gap: 8px;
    font-family: "Archivo Black", Arial, sans-serif;
    font-size: 20px;
    letter-spacing: 1px;
    text-transform: uppercase;
    color: var(--black);
  }
  .brand-small .brand-dot {
    width: 14px; height: 14px; border-radius: 50%;
    background: var(--red);
  }
  .brand-small-sub {
    position: absolute;
    left: 52px; top: 54px;
    font-family: "Archivo Black", Arial, sans-serif;
    font-size: 11px;
    letter-spacing: 4px;
    color: var(--black);
  }
  .contact-list {
    position: absolute;
    left: 30px; top: 120px;
    list-style: none;
  }
  .contact-list li {
    display: flex; align-items: center; gap: 10px;
    font-size: 14px;
    color: var(--black);
    margin-bottom: 9px;
  }
  .contact-icon {
    width: 20px; height: 20px;
    background: var(--red);
    border-radius: 3px;
    display: flex; align-items: center; justify-content: center;
    flex-shrink: 0;
  }
  .name-band {
    position: absolute;
    right: 0; top: 36px;
    width: 215px; height: 62px;
    background: var(--red);
    color: var(--white);
    padding: 10px 0 0 30px;
  }
  .name-band .person-name { font-size: 20px; font-weight: 700; }
  .name-band .person-title { font-size: 12px; margin-top: 2px; }
  .address {
    position: absolute;
    right: 60px; bottom: 48px;
    color: var(--white);
    font-size: 14px;
    line-height: 1.4;
    text-align: center;
  }
  .address svg { display: block; margin: 0 auto 4px; }
</style>
</head>
<body>

  <section class="card card-back">
    <div class="brand-large"><span class="brand-dot"></span>Keystone</div>
    <div class="brand-sub">Home Buyers</div>
    <div class="back-web">www.prairiehomeoffers.com</div>
  </section>

  <section class="card card-front">
    <svg class="front-shape" viewBox="0 0 525 300" preserveAspectRatio="none" aria-hidden="true">
      <polygon points="0,0 340,0 190,300 0,300" fill="#ffffff"/>
      <polygon points="330,36 310,60 310,98 330,98" fill="#ec1f27"/>
    </svg>

    <div class="brand-small"><span class="brand-dot"></span>Keystone</div>
    <div class="brand-small-sub">HOME BUYERS</div>

    <ul class="contact-list">
      <li>
        <span class="contact-icon">
          <svg width="12" height="12" viewBox="0 0 24 24"><path fill="#fff" d="M6.6 10.8a15.1 15.1 0 0 0 6.6 6.6l2.2-2.2c.3-.3.7-.4 1-.2 1.1.4 2.3.6 3.6.6.6 0 1 .4 1 1V20c0 .6-.4 1-1 1A17 17 0 0 1 3 4c0-.6.4-1 1-1h3.5c.6 0 1 .4 1 1 0 1.3.2 2.5.6 3.6.1.3 0 .7-.2 1z"/></svg>
        </span>555-014-2288
      </li>
      <li>
        <span class="contact-icon">
          <svg width="12" height="12" viewBox="0 0 24 24"><path fill="#fff" d="M2 5h20v14H2zm2 2v.5l8 5 8-5V7l-8 5z"/></svg>
        </span>dale@prairiehomeoffers.com
      </li>
      <li>
        <span class="contact-icon">
          <svg width="12" height="12" viewBox="0 0 24 24"><circle cx="12" cy="12" r="9" fill="none" stroke="#fff" stroke-width="2"/><path d="M3 12h18M12 3c3 3 3 15 0 18M12 3c-3 3-3 15 0 18" fill="none" stroke="#fff" stroke-width="1.6"/></svg>
        </span>www.prairiehomeoffers.com
      </li>
    </ul>

    <div class="name-band">
      <div class="person-name">Dale Marsh</div>
      <div class="person-title">President</div>
    </div>

    <div class="address">
      <svg width="12" height="16" viewBox="0 0 12 16"><path fill="#fff" d="M6 0a6 6 0 0 0-6 6c0 4.5 6 10 6 10s6-5.5 6-10a6 6 0 0 0-6-6zm0 8.5A2.5 2.5 0 1 1 6 3.5a2.5 2.5 0 0 1 0 5z"/></svg>
      P.O. Box 82<br>Meadowvale, KS 67100
    </div>
  </section>

</body>
</html>
```